Sunridge Wellness Circle Brochure*

Need 8.5 X 11" Trifold informational brochure to recruit participants for Countrywide Sunridge Wellness Circle that we offer in our office. This program led by bureau for public vitality (BPV). The flyer should provide information in a concise way, with graphic representation as much as possible and pleasant to read.

Colors

Designer to choose colors to be used in the design.

Requirements
Must have
• Less reading material, more graphical representation of the date in the info provided.
• I would like in a brochure style than flyer

```html
<!DOCTYPE html>
<html lang="en">
<head>
<meta charset="utf-8">
<title>Sunridge Wellness Circle Brochure</title>
<link href="https://fonts.googleapis.com/css2?family=Oswald:wght@500;700&family=Open+Sans:wght@400;600;700;800&display=swap" rel="stylesheet">
<style>
:root{
  --orange:#f39a1f;
  --blue:#1f74b3;
  --blue-dark:#15598c;
  --yellow:#ffe600;
  --green:#7cbf3b;
  --ink:#2b2b2b;
  --white:#ffffff;
  --page:#f2f2f2;
}
*{margin:0;padding:0;box-sizing:border-box}
html,body{width:739px;height:1200px;overflow:hidden;background:var(--page)}
body{position:relative;font-family:"Open Sans",Arial,sans-serif;color:var(--ink)}
.spread{position:absolute;left:26px;width:688px;background:var(--white);box-shadow:0 1px 4px rgba(0,0,0,.25);overflow:hidden}
.spread--outside{top:14px;height:540px}
.spread--inside{top:578px;height:608px}
.panel{position:absolute;top:0;height:100%;width:229px;overflow:hidden}
.p1{left:0}.p2{left:229px;width:230px}.p3{left:459px}
.photo{position:absolute}
.title{font-family:"Oswald",Impact,sans-serif;font-weight:700;text-transform:uppercase;line-height:1.02;text-align:center}

/* outside */
.lifestyle{position:absolute;left:14px;top:100px;right:12px}
.lifestyle h3{color:var(--blue);font-size:11px;font-weight:700;line-height:1.35;margin-bottom:8px}
.checks{list-style:none}
.checks li{display:flex;gap:6px;font-size:8.5px;line-height:1.25;margin-bottom:4px}
.checks svg{flex:none;margin-top:1px}
.p2.cover{background:var(--orange)}
.cover .title{position:absolute;top:145px;left:0;right:0;color:var(--white);font-size:22px}
.stats{position:absolute;top:250px;left:18px;right:18px;color:var(--white);text-align:center;font-size:8.5px;font-weight:600;line-height:1.35}
.stats p{margin-bottom:10px}
.front{background:var(--blue)}
.front .offer{position:absolute;top:14px;left:10px;right:10px;color:var(--white);font-weight:800;font-size:12px;text-align:center;line-height:1.2;text-transform:uppercase}
.front .title{position:absolute;top:78px;left:6px;right:6px;color:var(--yellow);font-size:27px}
.tagbox{position:absolute;right:10px;top:205px;width:92px;background:var(--white);text-align:center;padding:8px 4px;color:var(--blue);font-size:9px;font-weight:600;line-height:1.25}
.tagbox b{display:block;font-size:12px;font-weight:800}
.location{position:absolute;top:345px;left:10px;right:10px;text-align:center;color:var(--white)}
.location h4{color:var(--yellow);font-family:"Oswald",Impact,sans-serif;font-size:17px;font-weight:700;line-height:1.1}
.location .org{font-weight:700;font-size:11px;margin:6px 0 4px;line-height:1.25}
.location .addr{font-size:7.5px;line-height:1.3}
.location .phone{font-family:"Oswald",Impact,sans-serif;color:var(--yellow);font-size:26px;font-weight:700;margin-top:12px}
.location .web{font-size:10px;font-weight:700}

/* inside */
.inside-title{position:absolute;top:14px;left:10px;right:10px;color:var(--blue);font-size:19px;text-align:left}
.facts{position:absolute;top:70px;left:10px;right:10px;background:var(--blue);padding:10px 10px 6px;list-style:none}
.facts li{color:var(--white);font-size:7.5px;line-height:1.35;margin-bottom:7px;padding-left:12px;position:relative}
.facts li::before{content:"";position:absolute;left:0;top:3px;width:6px;height:6px;background:var(--yellow)}
.eligibility{position:absolute;top:345px;left:10px;right:10px;background:var(--blue);padding-bottom:8px}
.eligibility h4{background:var(--green);color:var(--white);font-size:15px;font-weight:800;text-align:center;padding:6px 0}
.eligibility .req{margin:8px 10px 0;background:var(--yellow);color:var(--blue-dark);font-weight:800;font-size:10px;text-align:center;padding:7px 4px;line-height:1.2;text-transform:uppercase}
.eligibility .or{color:var(--yellow);font-weight:800;font-size:11px;text-align:center;margin-top:6px}
.provides{position:absolute;top:80px;left:12px;right:10px}
.provides h3{color:var(--blue);font-size:12.5px;font-weight:800;line-height:1.3;margin-bottom:12px}
.provides li{font-size:9px;font-weight:700;line-height:1.25;margin-bottom:8px;color:var(--ink);text-transform:uppercase}
.provides li.plain{text-transform:none}
.learn{position:absolute;top:80px;left:12px;right:10px}
.learn h3{color:var(--blue);font-family:"Oswald",Impact,sans-serif;font-size:16px;font-weight:700;line-height:1.2;text-transform:uppercase;margin-bottom:12px}
.learn p{font-size:8.5px;font-weight:700;line-height:1.35;margin-bottom:8px;color:var(--ink);word-break:break-all}
</style>
</head>
<body>

<section class="spread spread--outside">
  <div class="panel p1">
    <div class="photo" style="left:0;top:0;width:229px;height:90px;background:linear-gradient(120deg,#e9ece6,#b9cf8f 45%,#d84b32 80%,#f2f2ee)" role="img" aria-label="Photo of fresh vegetables beside a scale and glucose meter"></div>
    <div class="lifestyle">
      <h3>Your patients will learn to make achievable and realistic lifestyle changes:</h3>
      <ul class="checks">
        <li><svg width="9" height="9" viewBox="0 0 10 10"><circle cx="5" cy="5" r="5" fill="#7cbf3b"/><path d="M2.6 5.2l1.6 1.6 3.2-3.4" stroke="#fff" stroke-width="1.4" fill="none"/></svg>Eat healthy</li>
        <li><svg width="9" height="9" viewBox="0 0 10 10"><circle cx="5" cy="5" r="5" fill="#7cbf3b"/><path d="M2.6 5.2l1.6 1.6 3.2-3.4" stroke="#fff" stroke-width="1.4" fill="none"/></svg>Incorporate physical activity into daily routine</li>
        <li><svg width="9" height="9" viewBox="0 0 10 10"><circle cx="5" cy="5" r="5" fill="#7cbf3b"/><path d="M2.6 5.2l1.6 1.6 3.2-3.4" stroke="#fff" stroke-width="1.4" fill="none"/></svg>Manage stress</li>
        <li><svg width="9" height="9" viewBox="0 0 10 10"><circle cx="5" cy="5" r="5" fill="#7cbf3b"/><path d="M2.6 5.2l1.6 1.6 3.2-3.4" stroke="#fff" stroke-width="1.4" fill="none"/></svg>Solve problems that get in the way of healthy changes</li>
      </ul>
    </div>
    <div class="photo" style="left:0;top:245px;width:229px;height:295px;background:linear-gradient(160deg,#f4f1ec,#e7d8c8 50%,#c98a6a)" role="img" aria-label="Photo of a smiling woman in a kitchen holding a healthy meal"></div>
  </div>

  <div class="panel p2 cover">
    <div class="photo" style="left:0;top:0;width:230px;height:130px;background:linear-gradient(135deg,#8fbf4a,#d9e3c6 45%,#e55a2b 75%,#f4c14a)" role="img" aria-label="Photo of vegetables around a Prevent Diabetes sign"></div>
    <h2 class="title">Countrywide<br>Sunridge Wellness<br>Circle</h2>
    <div class="stats">
      <p>86 million people – more than 1 out of 3 adults – have prediabetes.</p>
      <p>9 out of 10 don't know they have prediabetes.</p>
      <p>3 out of 10 Americans are expected to develop diabetes in their lifetime.</p>
      <p>Prediabetes increases your risk of type 2 diabetes, heart disease and stroke.</p>
    </div>
  </div>

  <div class="panel p3 front">
    <p class="offer">Maple Ridge Metabolic Care Center offers</p>
    <h1 class="title">Countrywide<br>Sunridge<br>Wellness Circle</h1>
    <div class="photo" style="left:0;top:185px;width:229px;height:145px;background:linear-gradient(110deg,#dfe9f1,#9fb9cc 55%,#6f8ea6)" role="img" aria-label="Photo of a doctor talking with a patient"></div>
    <div class="tagbox">Working together to prevent<b>TYPE 2 DIABETES</b></div>
    <div class="location">
      <h4>PROGRAM LOCATION:</h4>
      <p class="org">Maple Ridge Metabolic Care Center</p>
      <p class="addr">4200 Harbor Lane, Ste 12<br>Fairview, ST 00000</p>
      <p class="phone">555 210 4848</p>
      <p class="web">www.mapleridgecare.com</p>
    </div>
  </div>
</section>

<section class="spread spread--inside">
  <div class="panel p1">
    <h2 class="title inside-title">Countrywide Sunridge<br>Wellness Circle</h2>
    <ul class="facts">
      <li>Research shows modest lifestyle change, like losing weight and moving more, can halve type 2 risk.</li>
      <li>The Sunridge Wellness Circle is led by the bureau for public vitality (BPV) to curb diabetes.</li>
      <li>Losing 5 to 7% of body weight through diet and activity lowers diabetes risk by 58%.</li>
      <li>For people 60 and older, the program cut new type 2 cases by 71%.</li>
      <li>After 10 years, participants still had a one-third lower rate of type 2 diabetes.</li>
    </ul>
    <div class="eligibility">
      <h4>Patient Eligibility:</h4>
      <p class="req">18 years and older</p>
      <p class="req">Overweight</p>
      <p class="req">Previously diagnosed with gestational diabetes</p>
      <p class="or">OR</p>
      <p class="req" style="margin-top:6px">Diagnosed with prediabetes</p>
    </div>
  </div>

  <div class="photo" style="left:229px;top:0;width:459px;height:62px;background:linear-gradient(90deg,#d8432c,#f3a23a 20%,#9ccc4e 45%,#5f9d35 70%,#e8c24a 90%,#c83b2a)" role="img" aria-label="Photo strip of colourful fresh vegetables"></div>

  <div class="panel p2" style="top:62px;height:546px">
    <div class="provides" style="top:16px">
      <h3>A key part of the Sunridge Wellness Circle is a lifestyle change program that provides:</h3>
      <ul class="checks">
        <li><svg width="11" height="11" viewBox="0 0 10 10"><path d="M1 5.4l2.6 2.6L9 2" stroke="#7cbf3b" stroke-width="2" fill="none"/></svg>A trained lifestyle coach</li>
        <li><svg width="11" height="11" viewBox="0 0 10 10"><path d="M1 5.4l2.6 2.6L9 2" stroke="#7cbf3b" stroke-width="2" fill="none"/></svg>BPV-approved curriculum</li>
        <li><svg width="11" height="11" viewBox="0 0 10 10"><path d="M1 5.4l2.6 2.6L9 2" stroke="#7cbf3b" stroke-width="2" fill="none"/></svg>Group support over the course of a year</li>
        <li class="plain"><svg width="11" height="11" viewBox="0 0 10 10"><path d="M1 5.4l2.6 2.6L9 2" stroke="#7cbf3b" stroke-width="2" fill="none"/></svg>16 weekly meetings with monthly follow up</li>
      </ul>
    </div>
    <div class="photo" style="left:0;top:300px;width:230px;height:246px;background:linear-gradient(150deg,#f3efe6,#c9d99a 45%,#7fae45 75%,#e0703a)" role="img" aria-label="Photo of a healthy salad and vegetables on a table"></div>
  </div>

  <div class="panel p3" style="top:62px;height:546px">
    <div class="learn" style="top:16px">
      <h3>Learn more from BPV and take the prediabetes risk quiz at:</h3>
      <p>www.bpv.gov/vitality/basics/prediabetes.html</p>
      <p>www.bpv.gov/vitality/prevention</p>
      <p>www.bpv.gov/StayWell2</p>
    </div>
    <div class="photo" style="left:0;top:230px;width:229px;height:316px;background:linear-gradient(160deg,#f5f3ef,#e9dccd 45%,#e4553a 75%,#f1c64a)" role="img" aria-label="Photo of a cheerful girl holding sliced peppers in a kitchen"></div>
  </div>
</section>

</body>
</html>
```